PRP Poster

We need a poster for a doctors room to encourage people to enquire about PRP procedure.

It needs to include "for osteoarthritis and sports injuries" and "enhancing the body's natural ability to heal".

A brochure is attached which outlines what PRP (Platelet Rich Plasma) is, in the brochure it is called DVX. DO NOT USE ANY OF THE LOGOS FROM THIS BROCHURE.

Target Market(s)

patients in an orthopaedic surgery waiting room/area
age range from teenagers till 80year olds
male= female ratio

Requirements
Must have
• single poster
eye-catching yet professional
needs to be suitable/appropriate for the waiting area of a surgeons clinic
Nice to have
• prp is a natural therapy (it is essentially the person's own blood being reinjected to a site of injury)
the "natural" aspect of the therapy needs to be emphasised

```html
<!DOCTYPE html>
<html lang="en">
<head>
<meta charset="utf-8">
<title>Platelet Rich Plasma – Poster</title>
<link rel="stylesheet" href="https://fonts.googleapis.com/css2?family=Anton&family=Cabin:wght@500&family=Open+Sans:wght@400&family=PT+Sans:wght@400&family=PT+Sans+Narrow:wght@400;700&display=swap">
<style>
  :root {
    --bg-light: #f4f6f9;
    --bg-mid: #e6eaf0;
    --bg-edge: #cfd6e0;
    --ink: #111111;
    --accent: #e2470f;
    --accent-shadow: rgba(40, 20, 10, 0.75);
  }
  html, body {
    margin: 0;
    padding: 0;
    width: 800px;
    height: 1200px;
    overflow: hidden;
  }
  .poster {
    position: relative;
    width: 800px;
    height: 1200px;
    overflow: hidden;
    background:
      radial-gradient(ellipse 75% 60% at 50% 50%, var(--bg-light) 0%, var(--bg-mid) 65%, var(--bg-edge) 100%);
    color: var(--ink);
  }
  .indication {
    position: absolute;
    top: 64px;
    left: 0;
    width: 800px;
    margin: 0;
    text-align: center;
    font-family: "Cabin", sans-serif;
    font-weight: 500;
    font-size: 54px;
    line-height: 77px;
    color: var(--accent);
    text-shadow: 2px 2px 1px var(--accent-shadow);
    white-space: nowrap;
  }
  .title {
    position: absolute;
    top: 0;
    left: 0;
    width: 800px;
    height: 1200px;
  }
  .title text {
    font-family: "Anton", sans-serif;
  }
  .title .word-dark { fill: var(--ink); }
  .title .word-accent { fill: var(--accent); }
  .claim {
    position: absolute;
    top: 842px;
    left: 318px;
    margin: 0;
    font-family: "PT Sans Narrow", sans-serif;
    font-weight: 700;
    font-size: 36px;
    line-height: 40px;
    white-space: nowrap;
  }
  .claim-note {
    position: absolute;
    top: 891px;
    left: 318px;
    margin: 0;
    font-family: "PT Sans Narrow", sans-serif;
    font-size: 12.5px;
    line-height: 18px;
    white-space: nowrap;
  }
  .natural-note {
    position: absolute;
    top: 935px;
    left: 164px;
    margin: 0;
    font-family: "PT Sans", sans-serif;
    font-size: 16px;
    line-height: 20px;
    white-space: nowrap;
  }
  .tagline {
    position: absolute;
    top: 1038px;
    left: 0;
    width: 800px;
    margin: 0;
    text-align: center;
    font-family: "Open Sans", sans-serif;
    font-size: 49px;
    line-height: 60px;
    white-space: nowrap;
  }
</style>
</head>
<body>
<main class="poster">
  <h2 class="indication">FOR OSTEOARTHRITIS AND<br>SPORTS INJURIES</h2>

  <svg class="title" viewBox="0 0 800 1200" aria-labelledby="title-text">
    <title id="title-text">Platelet Rich Plasma</title>
    <text class="word-dark" x="150" y="420" font-size="140" textLength="497" lengthAdjust="spacingAndGlyphs">PLATELET</text>
    <text class="word-accent" x="155" y="690" font-size="291" textLength="485" lengthAdjust="spacingAndGlyphs">RICH</text>
    <text class="word-dark" x="150" y="840" font-size="157" textLength="497" lengthAdjust="spacingAndGlyphs">PLASMA</text>
  </svg>

  <p class="claim">PRP is a Natural Therapy</p>
  <p class="claim-note">(it is essentially the person's own Blood being reinjected to a site of injury)</p>
  <p class="natural-note">The "Natural" aspect of the therapy needs to be emphasised</p>

  <p class="tagline">"Enhancing the body's natural<br>ability to heal".</p>
</main>
</body>
</html>
```